Business Postcard Design for Personal Training Company

Need a postcard design for my company called "Maple Stride" Colors are Navy Blue, Blue, Grey and White.

On the front I want there to be pictures and it to feature a box that says "Free Consultation + 50% off your first session!"

And somehow to feature the following phrases " Lose Weight. Gain Muscle."
"Customized Personal training using Q-Pulse, the latest technology in fitness. Reach your fitness goals in just two 25-min sessions per week"

Also want featured the following phrases (maybe on back):

"up to 18 times more effective than a conventional gym workout"

I need the back of the postcard to have all my business information:

Address: 372 Dovercrest Ave, Building B Suite 218, Costa Mesa CA 92631
Website: maple-stride.example
Phone #: (949) 555-0137
E-mail: maplestridehealth@mailbox.example

I am going to upload my logo, before and after pictures and pictures of people training on the device. Feel free to use as many/or little photos as you want.

Target Market(s)

Wealthy Adults 40+ years old looking for a personal trainer

Industry/Entity Type

Personal Trainer

Colors
0455a3
85cae6
aaaaaa
ffffff

Requirements
Must have
• At least two of the before and after photos, and two or more photos of people working out on the device.

```html
<!DOCTYPE html>
<html lang="en">
<head>
<meta charset="utf-8">
<title>Maple Stride Postcard</title>
<link rel="stylesheet" href="https://fonts.googleapis.com/css2?family=Bebas+Neue&family=Lato:wght@400;700&display=swap">
<style>
  :root {
    --brand-blue: #009fd4;
    --navy: #0455a3;
    --charcoal: #3b3b3d;
    --paper: #ffffff;
    --backdrop: #ecedef;
    --rule-grey: #9a9a9a;
    --logo-grey: #6d6f73;
    --photo-green: #6f8f4a;
    --photo-sky: #b9c2c9;
    --photo-skin: #d9b79a;
    --photo-wall: #e6e3df;
  }
  * { margin: 0; padding: 0; box-sizing: border-box; }
  html, body {
    width: 1200px; height: 1200px; overflow: hidden;
    background: var(--backdrop);
  }
  .canvas { position: relative; width: 1200px; height: 1200px; }
  .postcard {
    position: absolute; left: 266px; width: 669px; height: 474px;
    box-shadow: 0 3px 10px rgba(0,0,0,0.18);
    background: var(--paper);
  }
  .postcard--back { top: 92px; }
  .postcard--front { top: 634px; }
  .postcard svg { display: block; width: 100%; height: 100%; }
  .heading { font-family: 'Bebas Neue', 'Oswald', sans-serif; }
  .body-text { font-family: 'Lato', sans-serif; }
</style>
</head>
<body>
<div class="canvas">

  <!-- Back: contact side -->
  <section class="postcard postcard--back">
    <svg viewBox="0 0 780 553" xmlns="http://www.w3.org/2000/svg">
      <defs>
        <linearGradient id="outdoorTraining" x1="0" y1="0" x2="0" y2="1">
          <stop offset="0" stop-color="var(--photo-sky)"/>
          <stop offset="0.35" stop-color="#4e6a3c"/>
          <stop offset="1" stop-color="var(--photo-green)"/>
        </linearGradient>
      </defs>
      <g role="img" aria-label="Photo of a client stretching in a training suit beside the trainer and device on a lawn">
        <polygon points="0,0 380,0 334,295 0,295" fill="url(#outdoorTraining)"/>
      </g>
      <line class="slant-rule" x1="386" y1="0" x2="304" y2="508" stroke="var(--rule-grey)" stroke-width="1.5"/>

      <!-- effectiveness claim -->
      <g class="claim">
        <text class="heading" x="590" y="200" font-size="30" fill="var(--charcoal)" text-anchor="middle" letter-spacing="1">UP TO</text>
        <text class="heading" x="590" y="270" font-size="78" fill="var(--brand-blue)" text-anchor="middle">18 TIMES</text>
        <text class="heading" x="590" y="306" font-size="30" fill="var(--navy)" text-anchor="middle" letter-spacing="0.5">MORE EFFECTIVE</text>
        <rect x="500" y="320" width="180" height="3" fill="var(--brand-blue)"/>
        <text class="body-text" x="590" y="348" font-size="16" fill="var(--charcoal)" text-anchor="middle">than a conventional gym workout</text>
      </g>

      <polygon class="contact-header" points="0,302 332,302 327,334 0,334" fill="var(--brand-blue)"/>
      <polygon class="contact-panel" points="0,334 327,334 300,508 0,508" fill="var(--charcoal)"/>
      <text class="heading" x="12" y="329" font-size="23" fill="var(--charcoal)" letter-spacing="0.3">CONTACT DETAILS :</text>

      <g fill="none" stroke="#fff" stroke-width="2">
        <path d="M20 349c-5 0-8 4-8 8 0 6 8 13 8 13s8-7 8-13c0-4-3-8-8-8z"/>
        <circle cx="20" cy="357" r="3"/>
      </g>
      <text class="body-text" x="39" y="362" font-size="16" fill="#fff">372 Dovercrest Ave, Building B Suite</text>
      <text class="body-text" x="39" y="382" font-size="16" fill="#fff">218, Costa Mesa CA 92631</text>

      <g fill="none" stroke="#fff" stroke-width="1.6">
        <circle cx="20" cy="407" r="8"/>
        <ellipse cx="20" cy="407" rx="3.5" ry="8"/>
        <line x1="12" y1="407" x2="28" y2="407"/>
      </g>
      <text class="body-text" x="39" y="414" font-size="16" fill="#fff">maple-stride.example</text>

      <g fill="#fff">
        <rect x="11" y="436" width="5" height="11" rx="1"/>
        <rect x="17" y="437" width="12" height="10" rx="1" fill="none" stroke="#fff" stroke-width="1.5"/>
        <rect x="20" y="440" width="6" height="1.5"/>
        <rect x="20" y="443" width="6" height="1.5"/>
      </g>
      <text class="body-text" x="39" y="447" font-size="16" fill="#fff">(949) 555-0137</text>

      <g fill="none" stroke="#fff" stroke-width="1.6">
        <rect x="11" y="467" width="18" height="13"/>
        <polyline points="11,467 20,475 29,467"/>
      </g>
      <text class="body-text" x="39" y="479" font-size="15" fill="#fff">maplestridehealth@mailbox.example</text>

      <rect class="base-rule" x="0" y="508" width="780" height="6" fill="var(--charcoal)"/>
      <rect class="base-band" x="0" y="514" width="780" height="39" fill="var(--brand-blue)"/>
    </svg>
  </section>

  <!-- Front: offer side -->
  <section class="postcard postcard--front">
    <svg viewBox="0 0 780 553" xmlns="http://www.w3.org/2000/svg">
      <defs>
        <linearGradient id="harbourTraining" x1="0" y1="0" x2="0" y2="1">
          <stop offset="0" stop-color="var(--photo-sky)"/>
          <stop offset="0.45" stop-color="#7f8a86"/>
          <stop offset="1" stop-color="var(--photo-green)"/>
        </linearGradient>
        <linearGradient id="progressPhoto" x1="0" y1="0" x2="0" y2="1">
          <stop offset="0" stop-color="var(--photo-wall)"/>
          <stop offset="1" stop-color="var(--photo-skin)"/>
        </linearGradient>
      </defs>
      <g role="img" aria-label="Photo of the trainer kneeling with dumbbells in a training suit beside the device, harbour behind">
        <polygon points="0,0 382,0 330,480 0,480" fill="url(#harbourTraining)"/>
      </g>

      <circle cx="503" cy="71" r="5" fill="var(--brand-blue)"/>
      <text class="body-text" x="515" y="77" font-size="17" font-weight="700" fill="var(--logo-grey)" letter-spacing="1">Maple Stride</text>

      <polygon class="headline-band" points="366,133 780,133 780,175 361,175" fill="var(--charcoal)"/>
      <text class="heading" x="579" y="166" font-size="28" fill="var(--brand-blue)" text-anchor="middle">LOSE WEIGHT . GAIN MUSCLE</text>

      <polygon class="intro-band" points="360,177 780,177 780,238 353,238" fill="var(--brand-blue)"/>
      <text class="heading" x="566" y="203" font-size="17" fill="var(--charcoal)" text-anchor="middle">CUSTOMIZED PERSONAL TRAINING USING Q-PULSE, THE LATEST TECHNOLOGY</text>
      <text class="heading" x="566" y="223" font-size="15.5" fill="var(--charcoal)" text-anchor="middle">IN FITNESS. REACH YOUR FITNESS GOALS IN JUST TWO 25-MIN SESSIONS PER WEEK</text>

      <g role="img" aria-label="Before photo of a client flexing one arm">
        <polygon points="346,241 562,241 524,480 313,480" fill="url(#progressPhoto)"/>
      </g>
      <g role="img" aria-label="After photo of the same client flexing, more toned">
        <polygon points="566,241 780,241 780,480 528,480" fill="url(#progressPhoto)"/>
      </g>
      <text class="heading" x="320" y="472" font-size="16" fill="var(--charcoal)">BEFORE</text>
      <text class="heading" x="547" y="472" font-size="16" fill="var(--charcoal)">AFTER</text>

      <rect class="base-rule" x="0" y="480" width="780" height="6" fill="var(--charcoal)"/>
      <rect class="offer-band" x="0" y="486" width="780" height="67" fill="var(--brand-blue)"/>
      <text class="heading" x="390" y="530" font-size="30" fill="#fff" text-anchor="middle">FREE CONSULTATION + 50% OFF YOUR FIRST SESSION!</text>
    </svg>
  </section>

</div>
</body>
</html>
```